Single-sided business card for restaurant bellwether with new logo made on this site

Business card options with new logo including restaurant name, address, phone number and website. This business card is single-sided only and will be presented at the hostess desk for clients to take. I would like to see options based on a cream card background, a white card background, a yellow card background and a burgundy colored background. It needs to be elegant and traditional.

Target Market(s)

local and international crowd

Industry/Entity Type

restaurant

Contact Information for Business Card

address, website and phone number

Font styles to use
Serif

Colors
EE7325
F08F49
F5BC92
FAE3D3
FDF4ED

Requirements
Must have
• new logo, address, phone number, website
Should not have
• more than three colors

```html
<!DOCTYPE html>
<html lang="es">
<head>
<meta charset="utf-8">
<title>Bellwether – Tarjeta de presentación</title>
<link rel="stylesheet" href="https://fonts.googleapis.com/css2?family=Cinzel:wght@500;600&family=EB+Garamond:wght@500&family=Arimo:wght@400&display=swap">
<style>
  :root {
    --backdrop: #c8c8c8;
    --card-yellow: #f7b52d;
    --ink-brown: #3e1a17;
  }
  * { margin: 0; padding: 0; box-sizing: border-box; }
  html, body {
    width: 1200px;
    height: 1200px;
    overflow: hidden;
    background: var(--backdrop);
  }
  .business-card {
    position: absolute;
    left: 294px;
    top: 100px;
    width: 612px;
    height: 1000px;
    background: var(--card-yellow);
    border: 1.5px solid var(--ink-brown);
    color: var(--ink-brown);
  }
  .brand-square {
    position: absolute;
    left: 223px;
    top: 172px;
    width: 196px;
    height: 197px;
    background: var(--ink-brown);
  }
  .brand-name {
    position: absolute;
    left: 0;
    width: 100%;
    text-align: center;
    font-family: "Cinzel", serif;
    font-weight: 600;
    font-size: 66px;
    line-height: 1;
    letter-spacing: 0.3em;
    text-indent: 0.3em;
  }
  .brand-name--top { top: 386px; }
  .brand-name--bottom { top: 455px; }
  .reservations-label {
    position: absolute;
    top: 600px;
    width: 100%;
    text-align: center;
    font-family: "Cinzel", serif;
    font-weight: 600;
    font-size: 36px;
    line-height: 1;
  }
  .reservations-phone {
    position: absolute;
    top: 640px;
    width: 100%;
    text-align: center;
    font-family: "EB Garamond", serif;
    font-weight: 500;
    font-size: 56px;
    line-height: 1;
  }
  .divider {
    position: absolute;
    left: 166px;
    width: 278px;
    height: 2px;
    background: linear-gradient(90deg, transparent, var(--ink-brown) 20%, var(--ink-brown) 80%, transparent);
  }
  .divider--upper { top: 707px; }
  .divider--lower { top: 900px; }
  .address {
    position: absolute;
    top: 731px;
    width: 100%;
    text-align: center;
    font-family: "Arimo", sans-serif;
    font-size: 28px;
    line-height: 37.5px;
    font-style: normal;
  }
  .website {
    position: absolute;
    top: 925px;
    width: 100%;
    text-align: center;
    font-family: "Arimo", sans-serif;
    font-size: 28px;
    line-height: 1;
  }
</style>
</head>
<body>
  <section class="business-card">
    <div class="brand-square"></div>
    <div class="brand-name brand-name--top">BELL</div>
    <div class="brand-name brand-name--bottom">WETHER</div>

    <div class="reservations-label">RESERVACIONES</div>
    <div class="reservations-phone">958-555-0142</div>

    <div class="divider divider--upper"></div>
    <address class="address">
      Restaurant Bell-Wether<br>
      Jacaranda 417<br>
      Bahías de Huatulco<br>
      Oaxaca CP 70990
    </address>
    <div class="divider divider--lower"></div>

    <div class="website">www.bellwether.com.mx</div>
  </section>
</body>
</html>
```